Book cover needed for self help business book

Book cover needed and I will provide back cover blurb and barcode to the winning designer. Book may be too small for spine, but I will give you the page number details to confirm. Book information below:

Title: Nine Winters a Trader
Subtitle: Proven Market Methods That Keep Paying Off Now
Author: Maribel Okonte

Design should be clean, modern, and bold—something that appeals to everyday entrepreneurs and resellers. The cover should reflect grit, real-world hustle, and long-term wisdom without looking overly corporate or flashy. I am open to your creative ideas.

I am open to modern designs, but also designs of rugged old covers that simulate a book that may have aged over the years.

I prefer not to have pictures or silhouettes of people

Requirements
Nice to have
• I am open to modern designs, but also designs of rugged old covers that simulate a book that may have aged over the years.
Should not have
• Pictures or silhouettes of people

```html
<!DOCTYPE html>
<html lang="en">
<head>
<meta charset="utf-8">
<title>Nine Winters a Trader — Book Cover</title>
<link rel="stylesheet" href="https://fonts.googleapis.com/css2?family=Montserrat:wght@600;700;800;900&display=swap">
<style>
  :root {
    --page-bg: #ffffff;
    --cover-bg: #070808;
    --grid-line: #262828;
    --accent-yellow: #fdbe23;
    --type-white: #ffffff;
  }
  html, body {
    margin: 0;
    padding: 0;
    width: 1200px;
    height: 1200px;
    overflow: hidden;
    background: var(--page-bg);
  }
  .canvas {
    display: block;
    width: 1200px;
    height: 1200px;
  }
  .cover-text {
    font-family: "Montserrat", Arial, sans-serif;
    text-anchor: middle;
  }
  .subtitle {
    fill: var(--type-white);
    font-weight: 600;
    font-size: 30px;
    letter-spacing: 1.5px;
  }
  .title-yellow {
    fill: var(--accent-yellow);
    font-weight: 900;
  }
  .title-white {
    fill: var(--type-white);
    font-weight: 900;
  }
  .title-rule {
    stroke: var(--type-white);
    stroke-width: 3;
    stroke-linecap: round;
  }
  .author {
    fill: var(--type-white);
    font-weight: 700;
    font-size: 34px;
    letter-spacing: 1px;
  }
  .cover-bg { fill: var(--cover-bg); }
  .grid-line { stroke: var(--grid-line); stroke-width: 1.5; fill: none; }
</style>
</head>
<body>
<svg class="canvas" viewBox="0 0 1200 1200" xmlns="http://www.w3.org/2000/svg">
  <defs>
    <pattern id="cover-grid" x="254" y="82" width="21.6" height="21.6" patternUnits="userSpaceOnUse">
      <path class="grid-line" d="M21.6 0 L0 0 L0 21.6"/>
    </pattern>
  </defs>

  <g class="book-cover">
    <rect class="cover-bg" x="254" y="82" width="692" height="1036"/>
    <rect x="254" y="82" width="692" height="1036" fill="url(#cover-grid)"/>

    <text class="cover-text subtitle" x="600" y="152">PROVEN MARKET METHODS THAT</text>
    <text class="cover-text subtitle" x="600" y="187">KEEP PAYING OFF NOW</text>

    <text class="cover-text title-yellow" x="600" y="545" font-size="285" textLength="598" lengthAdjust="spacingAndGlyphs">NINE</text>
    <text class="cover-text title-white" x="600" y="720" font-size="136" textLength="598" lengthAdjust="spacingAndGlyphs">WINTERS</text>

    <line class="title-rule" x1="306" y1="796" x2="539" y2="796"/>
    <line class="title-rule" x1="661" y1="796" x2="895" y2="796"/>
    <text class="cover-text title-white" x="600" y="825" font-size="82">A</text>

    <text class="cover-text title-yellow" x="600" y="947" font-size="122" textLength="600" lengthAdjust="spacingAndGlyphs">TRADER</text>

    <text class="cover-text author" x="600" y="1059">MARIBEL OKONTE</text>
  </g>
</svg>
</body>
</html>
```